Solar Flyer-Design
Zielgruppe
Quornel Energie
Für die Firma QuorNel Energie wird ein Flyer im Wickel oder Zickzackfalz Design benötigt. Größe soll Din Lang sein mit insgesamt 6 Seiten.
Es sollen die Inhalte der Webseite (quornel-energie.de bestmöglich verwendet werden.
Aufgabenstellung
Design anhand der Webseite, Bilder auch von der Webseite.
Logo befindet sich im Anhang und Bilder können frei von der Webseite genommen werden, wir besitzen alle Lizenzen daran.

```html
<!DOCTYPE html>
<html lang="de">
<head>
<meta charset="utf-8">
<title>Quornel Energie – Flyer DIN lang, Wickelfalz</title>
<link href="https://fonts.googleapis.com/css2?family=Poppins:wght@400;500;600;700;800&display=swap" rel="stylesheet">
<style>
  :root{
    --page:#e6e7e9;
    --blue:#1d9ee0;
    --navy:#2c4a8c;
    --green:#8cc63e;
    --orange:#e8951d;
    --ink:#33393f;
    --sky-top:#cfe6f6;
    --sky-bottom:#f4f8fb;
    --grass:#7fbf3a;
    --icon-bg:#f2c94c;
  }
  *{box-sizing:border-box;margin:0;padding:0}
  ul{list-style:none}
  html,body{width:1200px;height:900px;overflow:hidden}
  body{background:var(--page);font-family:"Poppins",sans-serif;color:var(--ink);position:relative}
  .sheet{position:absolute;left:300px;width:600px;height:424px;display:flex;box-shadow:0 6px 18px rgba(0,0,0,.18)}
  .sheet--outside{top:18px}
  .sheet--inside{top:458px}
  .panel{width:200px;height:424px;position:relative;overflow:hidden;display:flex;flex-direction:column;
    background:linear-gradient(180deg,var(--sky-top),var(--sky-bottom) 60%)}
  .panel + .panel{border-left:1px solid rgba(0,0,0,.06)}
  .panel--grey{background:linear-gradient(180deg,#e9ecef,#f7f8f9)}
  .head{background:var(--blue);color:#fff;font-weight:700;text-transform:uppercase;font-size:9px;line-height:1.15;padding:10px 10px 9px;margin-top:6px;position:relative}
  .head::after{content:"";position:absolute;right:18px;bottom:-6px;border:6px solid transparent;border-bottom:0;border-top-color:var(--blue)}
  .band{background:var(--green);color:#fff;font-weight:700;text-transform:uppercase;font-size:8.2px;line-height:1.15;padding:7px 10px;position:relative}
  .band::after{content:"";position:absolute;right:18px;bottom:-5px;border:5px solid transparent;border-bottom:0;border-top-color:var(--green)}
  .copy{font-size:5.6px;line-height:1.55;padding:0 10px;margin-top:7px}
  .copy strong{font-weight:700}
  .copy--accent{color:var(--blue);font-weight:700;text-transform:uppercase}
  .navy-box{background:var(--navy);color:#fff;font-size:5.4px;line-height:1.5;padding:8px 12px;margin:9px 10px 0}
  .navy-box p + p{margin-top:6px}
  .art{margin:6px 10px 0;border-radius:3px}
  .art--roof{height:64px;background:linear-gradient(180deg,#e3d2c8 0,#c9d2e4 60%,#dfeaf4)}
  .art--people{flex:1;margin:8px 0 0;border-radius:0;background:linear-gradient(180deg,var(--sky-bottom) 0,#dff0c9 45%,var(--grass) 100%)}
  .art--house{height:90px;background:linear-gradient(180deg,#e6edf0,#c9d8c4 70%,#9bc66e)}
  .art--city{flex:1;margin:8px 10px 8px;background:linear-gradient(180deg,#eef1f2,#d7dfcf 70%,#a6c77a)}
  .art--energy{height:88px;background:linear-gradient(180deg,#eaf4fb,#dfe9e4 70%,#a5cc79)}
  .services{margin-top:70px;text-align:center;color:var(--navy);font-weight:600;text-transform:uppercase;font-size:5.6px;line-height:1.35;display:flex;flex-direction:column;gap:9px;padding:0 14px}
  .brand{font-weight:700;color:var(--ink);letter-spacing:.5px;text-align:center;display:flex;align-items:center;justify-content:center;gap:5px}
  .brand__dot{width:7px;height:7px;background:var(--green);border-radius:50%}
  .brand--mid{margin-top:44px;font-size:12px}
  .brand--cover{margin-top:26px;font-size:13px}
  .url{font-size:6.5px;text-align:center;margin-top:6px}
  .solar-field{margin-top:auto;height:150px;background:linear-gradient(180deg,rgba(244,248,251,0) 0,#b7c6df 45%,#a9c98a 85%,var(--grass))}
  .cover-title{color:var(--navy);font-weight:800;text-transform:uppercase;text-align:center;font-size:10.5px;line-height:1.2;margin-top:20px;padding:0 8px}
  .callout{background:var(--green);color:#fff;font-size:6.6px;line-height:1.3;text-align:right;padding:6px 9px;margin:18px 0 0 38px}
  .art--cover{margin:0;border-radius:0;flex:1;background:linear-gradient(180deg,#dbe9f3 0,#7f93b8 35%,#3e5688 65%,#8fbf5a 90%,var(--grass))}
  .reasons{background:var(--orange);color:#fff;padding:8px 10px;margin-top:8px}
  .reasons h3{font-size:6.6px;font-weight:700;text-transform:uppercase;margin-bottom:4px}
  .reasons li{font-size:4.7px;line-height:1.35;padding-left:9px;position:relative;margin-top:3px}
  .reasons li::before{content:"";position:absolute;left:0;top:1px;width:5px;height:5px;background:#fff;border-radius:1px}
  .reasons li::after{content:"";position:absolute;left:1px;top:2px;width:3px;height:1.5px;border-left:1px solid var(--orange);border-bottom:1px solid var(--orange);transform:rotate(-45deg)}
  .fine{font-size:4.4px;line-height:1.45;padding:7px 10px 0}
  .surfaces{display:flex;justify-content:space-around;padding:10px 6px 0}
  .surfaces figure,.factors figure{text-align:center;font-size:3.9px;text-transform:uppercase;font-weight:500}
  .icon{display:block;margin:0 auto 2px;width:14px;height:14px;border-radius:3px;background:var(--icon-bg)}
  .factors{display:grid;grid-template-columns:repeat(3,1fr);row-gap:12px;padding:14px 8px 0}
  .factors .icon{width:18px;height:18px;border-radius:50%}
  .foot-line{margin-top:auto;height:4px;background:var(--blue)}
  .copy--lead{margin-top:14px}
  .band--factors{margin-top:12px}
</style>
</head>
<body>

<section class="sheet sheet--outside" aria-label="Außenseite">
  <article class="panel">
    <h2 class="head">Die Erträge fallen niedriger aus, wenn die Dachneigung unter 35 Grad und über 40 Grad liegt.</h2>
    <div class="art art--roof" role="img" aria-label="Ziegeldach mit Solarmodulen"></div>
    <p class="copy">Eine Dachneigung von 35 bis 40 Grad ist optimal für hohe Erträge. Auf Flachdächern kann eine Aufständerung der Photovoltaik Module erfolgen.</p>
    <p class="copy">Eine Montage der Module an der Fassade ist möglich, wenn die Sonneneinstrahlung an der Fassade entsprechend hoch ist. Die Erträge liegen allerdings deutlich niedriger als bei der Dachmontage.</p>
    <div class="navy-box">
      <p>Wir installieren Photovoltaik-Anlagen mit einer Leistung von bis zu 30 kWp für Privatkunden.</p>
      <p>Für gewerbliche Kundeninstallieren wir Photovoltaik-Anlagen mit einer Leistung von bis zu 500 kWp.</p>
    </div>
    <div class="art art--people" role="img" aria-label="Illustration: Personen mit Glühbirne und Solarmodulen auf einer Wiese"></div>
  </article>

  <article class="panel">
    <ul class="services">
      <li>Intelligentes<br>Energie-Management</li>
      <li>Alle Leistungen<br>aus einer Hand</li>
      <li>Notstromfähige Wechselrichter<br>und Insellösungen</li>
      <li>Hochwertige Photovoltaik<br>Module aus der EU</li>
    </ul>
    <div class="brand brand--mid"><span class="brand__dot"></span>QUORNEL ENERGIE</div>
    <p class="url">quornel-energie.de</p>
    <div class="solar-field" role="img" aria-label="Foto: Solarmodule vor Wiese"></div>
  </article>

  <article class="panel">
    <div class="brand brand--cover"><span class="brand__dot"></span>QUORNEL ENERGIE</div>
    <h1 class="cover-title">Saubere Stromerzeugung mithilfe von einer Photovoltaik-Anlage.</h1>
    <p class="callout">Möchtest Du Deinen eigenen Strom erzeugen und unabhängiger werden?</p>
    <div class="art art--cover" role="img" aria-label="Foto: blaues Holzhaus mit Solardach auf grüner Wiese"></div>
  </article>
</section>

<section class="sheet sheet--inside" aria-label="Innenseite">
  <article class="panel panel--grey">
    <h2 class="head">Photovoltaikanlage eine saubere und umweltfreundliche Lösung.</h2>
    <div class="art art--house" role="img" aria-label="Illustration: Haus mit Solardach und Person"></div>
    <p class="copy">Bei uns als Full-Service-Anbieter für PV-Anlagen, für private und gewerbliche Kunden, bist Du an der richtigen Adresse. Gemeinsam mit uns kannst Du Deine PV Anlage planen, abhängig von den örtlichen Gegebenheiten und Deinem Stromverbrauch.</p>
    <p class="copy copy--accent">Den erzeugten Strom kannst Du selbst nutzen, um Stromkosten zu sparen und/oder ihn an den örtlichen Stromnetzbetreiber verkaufen.</p>
    <p class="copy">Mit einer vollumfänglichen PV-Anlage (z.B. mit einem Speicher) senkst Du deine Energiekosten.</p>
    <div class="art art--city" role="img" aria-label="Illustration: Stadt und Industrie mit Solarfeldern"></div>
  </article>

  <article class="panel">
    <div class="art art--energy" role="img" aria-label="Illustration: Haus mit Solardach, Batterie und Elektroauto"></div>
    <h2 class="band">Selbst zum Stromerzeuger werden mit der</h2>
    <p class="copy">Du hast ein Eigenheim und/oder besitzt Immobilien mit genügend Platz auf dem Dach, dann ist eine Photovoltaik-Anlage eine gute Option.</p>
    <div class="reasons">
      <h3>Dafür gibt es mehrere gute Gründe:</h3>
      <ul>
        <li>Du wirst unabhängiger von den öffentlichen Stromanbietern</li>
        <li>Du leistest einen Beitrag zur Energiewende und zum Klimaschutz</li>
        <li>Photovoltaik ist eine saubere Form der Energieerzeugung, da keine Schadstoffe ausgestoßen werden</li>
        <li>Einspeisevergütung wird gezahlt, wenn der Strom in ein öffentliches Netz verkauft wird</li>
        <li>Du sparst Stromkosten, wenn Du den Strom selbst nutzt</li>
        <li>Eine PV Anlage kann mit Elektromobilität kombiniert werden</li>
        <li>PV-Anlagen kommen mit wenig Wartung aus</li>
        <li>Lebensdauer einer PV-Anlage liegt bei ca. 20 bis 25 Jahren</li>
        <li>Förderung für die Errichtung von PV-Anlagen ist möglich</li>
      </ul>
    </div>
    <p class="fine">Die Einsparung pro Kilowattstunde Strom aus der PV-Anlage, den Du selbst nutzt, ist deutlich höher als die zu erwartende Einspeisevergütung. <strong>Entscheidest Du Dich für eine vollumfängliche PV-Anlage mit Speicher, so kannst Du deinen Strombedarf selbst erzeugen,</strong> speichern und den Strom auch dann nutzen, wenn die Sonne nicht scheint.</p>
  </article>

  <article class="panel">
    <h2 class="head">Die Installation von Photovoltaikanlagen auf verschiedenen Flächen</h2>
    <p class="copy copy--lead">Eine Photovoltaikanlage kann nicht nur auf dem Dach Deines Hauses installiert werden, sondern auch auf Garagen, Carports Industriedächern und Freiflächen. So lassen sich komplette Solarparks errichten. Die PV-Modul Dachmontage solte so erfolgen, dass die Erträge an Strom möglichst hoch sind.</p>
    <p class="copy"><strong>Optimal ist ein Dach mit Südausrichtung, doch geeignet sind auch Dächer mit Südwest-, Südost- und Ostwest Ausrichtung, allerdings fallen die Erträge dann geringer aus.</strong></p>
    <div class="surfaces">
      <figure><span class="icon" role="img" aria-label="Symbol Garage"></span>Garage</figure>
      <figure><span class="icon" role="img" aria-label="Symbol Dächer"></span>Dächer</figure>
      <figure><span class="icon" role="img" aria-label="Symbol Carport"></span>Carport</figure>
      <figure><span class="icon" role="img" aria-label="Symbol Industrieflächen"></span>Industrieflächen</figure>
    </div>
    <h2 class="band band--factors">Die Energieerzeugungserträge hängen von verschiedenen Faktoren ab:</h2>
    <div class="factors">
      <figure><span class="icon" role="img" aria-label="Symbol Kompass"></span>Ausrichtung des Daches</figure>
      <figure><span class="icon" role="img" aria-label="Symbol Winkel"></span>Dachneigung</figure>
      <figure><span class="icon" role="img" aria-label="Symbol Wetter"></span>Witterung</figure>
      <figure><span class="icon" role="img" aria-label="Symbol Sonne und Module"></span>Sonneneinstrahlung</figure>
      <figure><span class="icon" role="img" aria-label="Symbol Karte"></span>Region</figure>
      <figure><span class="icon" role="img" aria-label="Symbol Schatten"></span>Beschattung</figure>
    </div>
    <div class="foot-line"></div>
  </article>
</section>

</body>
</html>
```